QV - menu design

Hi,

We require elegant menu design for upscale restaurant. Please find attached the logo and the menu items for your reference.

for inspiration, this is a good website: -
http://www.platewhisper.example/bellfoldnotes/about.php

We are very much open for Menu Size suggestions.

unfortunately the place is going under renovation, we don't have updated images to it. the closest look and feel to our place is http://varnelo.example ..

we are also open for creative options on the shape, the styles, etc. as long as it represents the fine dine feel ...

Thanks ...

Dear All,

We wouldlike to extend our apology for not being able to provide feedbacks on everysingle design. We were extremely busy and we have multiple contests opensimultaneously which makes the process even harder.

However,we would like to thank you all for the efforts you have put into designingour menu. It is very much appreciated …

We wishyou all success in your design ventures and we are quite positive that we willbe working with many of you on many projects in the soon future. 

Thanks & Regards,

TLG Team...

 

 

 

Industry/Entity Type

Restaurant

Requirements
Must have
• Please ensure that there are 'some' images in the menu ... this is very important.
Should not have
• IMPORTANT: -

1. Please DO NOT insert any currency sign to the menu
2. Please keep the prices of the menu at the end of the menu items descriptions NOT beside the menu item names. The font of the price should be similar to the menu item description and please DO NOT bold the numbers. the prices should be subtle.

Thank you ...

```html
<!DOCTYPE html>
<html lang="en">
<head>
<meta charset="utf-8">
<title>QV – Menu</title>
<link rel="stylesheet" href="https://fonts.googleapis.com/css2?family=Cormorant+Garamond:ital,wght@0,500;1,400;1,500;1,600&family=Josefin+Sans:wght@400&display=swap">
<style>
  :root {
    --backdrop: #e7e7e5;
    --ink: #0d0c0b;
    --paper: #ffffff;
    --tan: #a8896a;
    --tan-light: #c7a984;
    --cream: #ece6dc;
    --frame-gap: 14px;
  }
  * { box-sizing: border-box; margin: 0; padding: 0; }
  html, body {
    width: 1200px;
    height: 3380px;
    overflow: hidden;
  }
  body {
    background: var(--backdrop);
    position: relative;
    font-family: "Cormorant Garamond", Georgia, serif;
  }

  /* ---------- Cover ---------- */
  .cover {
    position: absolute;
    left: 350px;
    top: 70px;
    width: 500px;
    height: 1500px;
    box-shadow: 0 18px 40px rgba(0,0,0,0.18);
  }
  .cover-shape { position: absolute; inset: 0; display: block; }
  .cover-name {
    position: absolute;
    top: 130px;
    left: 0;
    width: 100%;
    text-align: center;
    font-family: "Josefin Sans", Arial, sans-serif;
    font-weight: 400;
    font-size: 40px;
    line-height: 1.25;
    letter-spacing: 8px;
    text-transform: uppercase;
    color: var(--ink);
  }
  .cover-title {
    position: absolute;
    top: 820px;
    left: 0;
    width: 100%;
    text-align: center;
    font-style: italic;
    font-weight: 500;
    font-size: 118px;
    color: var(--tan);
    letter-spacing: 2px;
  }

  /* ---------- Inside spread ---------- */
  .spread {
    position: absolute;
    left: 70px;
    top: 1680px;
    width: 1060px;
    height: 1620px;
    display: flex;
    box-shadow: 0 18px 40px rgba(0,0,0,0.2);
  }
  .panel {
    width: 530px;
    height: 100%;
    background: var(--ink);
    border: var(--frame-gap) solid var(--tan);
    padding: 34px 40px 36px;
    display: flex;
    flex-direction: column;
  }
  .panel + .panel { border-left-width: 7px; }
  .panel:first-child { border-right-width: 7px; }

  .section-title {
    font-style: italic;
    font-weight: 600;
    font-size: 46px;
    color: var(--tan-light);
    margin-bottom: 18px;
  }
  .menu-list {
    list-style: none;
    display: flex;
    flex-direction: column;
    gap: 20px;
  }
  .menu-item-name {
    font-style: italic;
    font-weight: 600;
    font-size: 28px;
    color: var(--tan-light);
    line-height: 1.15;
  }
  .menu-item-desc {
    font-style: italic;
    font-weight: 400;
    font-size: 20px;
    line-height: 1.3;
    color: var(--cream);
    margin-top: 3px;
  }
  .menu-list.compact { gap: 14px; }
  .menu-list.compact .menu-item-name { font-size: 26px; }
  .menu-list.compact .menu-item-desc { font-size: 19px; }

  .photo {
    border: 3px solid var(--tan);
    flex-shrink: 0;
  }
  .photo-breakfast {
    margin-top: auto;
    height: 400px;
    background: radial-gradient(ellipse at 40% 60%, #e9d7c6 0%, #b58a66 35%, #4a3325 75%, #231811 100%);
  }
  .photo-seafood {
    height: 270px;
    margin: 24px 0 20px;
    background: radial-gradient(ellipse at 55% 55%, #f2efe8 0%, #c8c4b8 30%, #7d8fa6 60%, #2d3948 100%);
  }
  .soups .section-title { margin-bottom: 12px; }
</style>
</head>
<body>

  <section class="cover" aria-label="Menu cover">
    <svg class="cover-shape" viewBox="0 0 500 1500" width="500" height="1500" aria-hidden="true">
      <rect width="500" height="1500" fill="var(--paper)"/>
      <polygon points="0,318 250,402 500,318 500,1500 0,1500" fill="var(--tan)"/>
      <polygon points="14,336 250,416 486,336 486,1486 14,1486" fill="var(--ink)"/>
    </svg>
    <p class="cover-name">Marlow Lane<br>Café</p>
    <h1 class="cover-title">Menu</h1>
  </section>

  <section class="spread" aria-label="Menu inside">
    <article class="panel breakfast">
      <h2 class="section-title">Breakfast</h2>
      <ul class="menu-list">
        <li><p class="menu-item-name">Butter Croissant</p>
          <p class="menu-item-desc">Served plain with a selection of preserves, creamy butter and honey, 18</p></li>
        <li><p class="menu-item-name">Classic Crepes</p>
          <p class="menu-item-desc">Crumbly buttery crepes with chocolate filling, 24</p></li>
        <li><p class="menu-item-name">Daily Fresh Eggs</p>
          <p class="menu-item-desc">Your choice of eggs, poached, fried or scrambled, served with toast, 32</p></li>
        <li><p class="menu-item-name">Healthy Time</p>
          <p class="menu-item-desc">Fresh fruit salad with low fat yogurt, honey and toasted granola, 28</p></li>
        <li><p class="menu-item-name">Energy Time</p>
          <p class="menu-item-desc">A fresh juice of your choice served with pancakes, maple syrup, berries and whipped cream on the side, 36</p></li>
        <li><p class="menu-item-name">House Morning Time</p>
          <p class="menu-item-desc">Two eggs any style, grilled sausage, hash browns, beans, toast and a hot drink of your choice, 42</p></li>
        <li><p class="menu-item-name">The Classic Breakfast</p>
          <p class="menu-item-desc">Eggs benedict on a toasted muffin with smoked salmon and juice, 45</p></li>
      </ul>
      <div class="photo photo-breakfast" role="img" aria-label="Photo of a set breakfast table with orange juice, cups and pastries"></div>
    </article>

    <article class="panel sandwiches">
      <h2 class="section-title">The Sandwiches</h2>
      <ul class="menu-list compact">
        <li><p class="menu-item-name">Grilled Vegetables Sandwich</p>
          <p class="menu-item-desc">Grilled zucchini, eggplant and peppers with pesto on ciabatta, 30</p></li>
        <li><p class="menu-item-name">Beef Burger</p>
          <p class="menu-item-desc">Prime beef patty, cheddar, lettuce, tomato and pickles, 38</p></li>
        <li><p class="menu-item-name">Club Sandwich</p>
          <p class="menu-item-desc">Turkey, beef bacon, fried egg, lettuce and tomato, 34</p></li>
        <li><p class="menu-item-name">Tuna Sandwich</p>
          <p class="menu-item-desc">Tuna with sweet corn, celery and light mayonnaise, 29</p></li>
        <li><p class="menu-item-name">Fish Fillet Sandwich</p>
          <p class="menu-item-desc">Crispy fillet with tartar sauce and fresh greens, 35</p></li>
        <li><p class="menu-item-name">Roast Beef Sandwich</p>
          <p class="menu-item-desc">Thin sliced roast beef with mustard cream, 39</p></li>
        <li><p class="menu-item-name">Chicken Sandwich</p>
          <p class="menu-item-desc">Grilled chicken breast, rocket and sun dried tomatoes, 33</p></li>
      </ul>
      <div class="photo photo-seafood" role="img" aria-label="Photo of a seafood plate with mussels and vegetables on a white dish"></div>
      <div class="soups">
        <h2 class="section-title">Soups</h2>
        <ul class="menu-list compact">
          <li><p class="menu-item-name">Bouillabaisse</p>
            <p class="menu-item-desc">Provençal fish stew with saffron and rouille, 40</p></li>
          <li><p class="menu-item-name">Lentil Soup</p>
            <p class="menu-item-desc">Red lentils, cumin, lemon and crispy bread, 22</p></li>
          <li><p class="menu-item-name">Beef Soup</p>
            <p class="menu-item-desc">Slow cooked beef with root vegetables and herbs, 27</p></li>
        </ul>
      </div>
    </article>
  </section>

</body>
</html>
```